TMVG Website

Hi we require a website with similar attributes and design to this http://layout7.fernquaysites.com but obviously with all our information and images etc... also attached are our logos please do the design with the yellow logo not the red.

```html
<!DOCTYPE html>
<html lang="en">
<head>
<meta charset="utf-8">
<title>TMVG – Custom Wheels &amp; Tires</title>
<link href="https://fonts.googleapis.com/css2?family=Montserrat:wght@400;600;700;800&family=Open+Sans:wght@400;600&display=swap" rel="stylesheet">
<style>
:root{
  --red:#c7321c;
  --dark:#2a2a2a;
  --darker:#1e1e1e;
  --ink:#222;
  --muted:#777;
  --light:#f2f2f2;
  --line:#e2e2e2;
  --white:#fff;
}
*{box-sizing:border-box;margin:0;padding:0}
html,body{width:1200px;height:4878px;overflow:hidden}
body{font-family:"Open Sans",Arial,sans-serif;color:var(--ink);background:var(--white);position:relative}
h1,h2,h3,h4,.btn,.nav a{font-family:"Montserrat",Arial,sans-serif}
.abs{position:absolute}
.btn{display:inline-block;background:var(--dark);color:#fff;font-size:9px;font-weight:700;letter-spacing:.5px;padding:7px 20px;border-radius:14px;text-transform:uppercase;white-space:nowrap}
.btn.red{background:var(--red)}
.eyebrow{font-family:"Montserrat",sans-serif;color:var(--red);font-size:10px;font-weight:600;text-transform:uppercase;letter-spacing:1px;text-align:center}
.sec-title{font-size:25px;font-weight:700;text-align:center;text-transform:uppercase;color:var(--ink)}
.ph{background:linear-gradient(135deg,#9a9a9a,#4a4a4a)}
.small{font-size:10px;line-height:1.55;color:var(--muted)}

/* header + hero */
.hero{top:0;left:0;width:1200px;height:455px;background:radial-gradient(circle at 75% 35%,#8a8a8a,#3a3a3a 55%,#1a1a1a)}
.hero-wheel{top:0;left:0;width:1200px;height:455px}
.header{top:0;left:0;width:1200px;height:81px}
.logo{top:6px;left:16px;width:180px;height:66px;background:#111;display:flex;align-items:center;justify-content:center;gap:10px;color:#fff;font-family:"Montserrat",sans-serif;font-weight:800;font-size:26px;letter-spacing:2px}
.logo i{width:14px;height:14px;background:var(--red);display:block}
.nav{top:30px;left:650px;display:flex;gap:20px;align-items:center}
.nav a{color:#fff;font-size:10px;font-weight:600;text-decoration:none;text-transform:uppercase}
.nav a.on{color:var(--red)}
.phone-pill{top:24px;left:1082px;height:24px;width:78px;border-radius:12px;background:#333;color:#fff;font-size:9px;font-weight:700;display:flex;align-items:center;justify-content:center;gap:5px;font-family:"Montserrat",sans-serif}
.hero h1{top:218px;left:0;width:1200px;text-align:center;color:#fff;font-size:36px;font-weight:800;line-height:1.2;text-transform:uppercase}
.dots{top:425px;left:580px;display:flex;gap:6px}
.dots span{width:8px;height:8px;border-radius:50%;background:#fff;opacity:.5}
.dots span:first-child{opacity:1}

/* category strip */
.cats{top:455px;left:0;width:1200px;height:163px;background:var(--light);display:flex}
.cat{flex:1;display:flex}
.cat .ph{width:175px;height:163px;flex:none}
.cat-text{padding:18px 20px 0}
.cat-text h3{font-size:20px;font-weight:600;margin-bottom:6px}
.cat-text p{font-size:8px;line-height:1.5;color:var(--muted);margin-bottom:12px;width:150px}

/* who we are */
.who{top:683px;left:228px;width:731px;height:260px;background:var(--light);display:flex}
.who-text{width:340px;padding:40px 36px}
.who-text h2{font-size:24px;font-weight:700;margin:4px 0 14px}
.who-text .eyebrow{text-align:left}
.who-text p{margin-bottom:20px}
.who .ph{flex:1;background:linear-gradient(135deg,#d8d8d8,#b52a1a 55%,#6a1208)}

/* finder */
.finder{top:1014px;left:0;width:1200px;height:312px;background:linear-gradient(180deg,#2b3240,#151922)}
.finder h2{top:62px;width:1200px;text-align:center;color:#fff;font-size:25px;font-weight:700;text-transform:uppercase}
.finder p{top:100px;width:1200px;text-align:center;color:#ccc;font-size:10px}
.selects{top:148px;left:234px;display:flex;gap:20px}
.sel{width:170px;height:26px;background:#fff;border-radius:13px;display:flex;align-items:center;justify-content:space-between;padding:0 12px;font-size:9px;color:#555;font-family:"Montserrat",sans-serif;font-weight:600}
.sel::after{content:"";border:4px solid transparent;border-top-color:#555;margin-top:4px}
.finder .btn{top:202px;left:573px}

/* offer */
.offer{top:1398px;left:0;width:1200px;height:470px;background:var(--light)}
.cards3{left:234px;display:flex;gap:22px}
.card{width:228px;background:#fff}
.card .ph{height:162px}
.card-body{padding:18px 22px 22px;text-align:center}
.card-body h4{font-size:13px;font-weight:700;margin-bottom:8px}
.card-body p{margin-bottom:14px;font-size:8.5px}

/* why */
.why{top:1918px;left:0;width:1200px;height:340px}
.why .ph{top:80px;left:460px;width:285px;height:250px;border-radius:50%;background:radial-gradient(circle,#bbb,#3a3a3a 60%,#b52a1a 62%,#fff 70%)}
.feat{width:230px}
.feat h4{font-size:14px;font-weight:700;margin-bottom:5px}
.num{width:26px;height:26px;border-radius:50%;border:1px solid #bbb;display:flex;align-items:center;justify-content:center;font-size:11px;font-weight:700;font-family:"Montserrat",sans-serif}

/* split banner */
.split{top:2282px;left:0;width:1200px;height:399px}
.split h2{color:#fff;font-size:28px;font-weight:800;line-height:1.1;text-transform:uppercase}
.split p{color:#fff;font-size:12px;font-weight:600;line-height:1.4;width:230px;margin:10px 0 20px}
.btn.ghost{background:transparent;border:1px solid #fff}

/* products */
.products{left:0;width:1200px}
.prow{display:flex;gap:24px;position:absolute;left:234px}
.prod{width:170px;background:#fff;border:1px solid var(--line)}
.prod .ph{height:163px;background:radial-gradient(circle,#c8c8c8 0,#555 45%,#e9e9e9 47%)}
.prod-body{text-align:center;padding:12px 8px 14px}
.prod-body h4{font-size:11px;font-weight:700;line-height:1.3;text-transform:uppercase}
.price{color:var(--red);font-family:"Montserrat",sans-serif;font-weight:700;font-size:14px;margin:7px 0 8px}

/* video */
.video{top:3656px;left:0;width:1200px;height:446px;background:linear-gradient(90deg,#222,#3b3b3b 50%,#222)}
.video h2{top:8px;width:1200px;text-align:center;color:#fff;font-size:25px;font-weight:700;text-transform:uppercase;line-height:1.2}
.vbox{top:48px;left:406px;width:390px;height:370px}
.vbox .ph{height:250px;background:linear-gradient(135deg,#8a8a8a,#3a3a3a)}
.play{top:112px;left:175px;width:40px;height:28px;border-radius:6px;background:var(--red)}
.vbox p{color:#fff;font-size:11px;text-align:center;margin:16px 40px 12px}

/* customers */
.cust{top:4160px;left:0;width:1200px;height:340px}
.cust .row{top:81px;left:234px;display:flex;gap:22px}
.cust .ph{width:228px;height:153px;background:linear-gradient(135deg,#d9d9d9,#8a8a8a)}

/* partners */
.partners{top:4518px;left:0;width:1200px;height:136px;display:flex;justify-content:center;align-items:center;gap:60px;border-top:1px solid var(--line)}
.badge{width:66px;height:66px;border-radius:50%;border:2px solid #999}

/* footer */
.footer{top:4654px;left:0;width:1200px;height:224px;background:var(--darker);color:#aaa}
.fcol{top:40px}
.fcol h4{color:#fff;font-size:13px;font-weight:700;margin-bottom:14px}
.fcol p,.fcol li{font-size:9px;line-height:1.8;list-style:none}
.flinks{display:flex;gap:30px}
.flogo{color:#fff;font-family:"Montserrat",sans-serif;font-weight:800;font-size:20px;display:flex;gap:8px;align-items:center;margin-bottom:12px}
.flogo i{width:10px;height:10px;background:var(--red);display:block}
.news{display:flex;gap:6px;align-items:center}
.news-field{width:140px;height:24px;background:#fff;border-radius:12px;font-size:9px;color:#777;padding:6px 12px}
.fbar{top:182px;left:0;width:1200px;height:42px;border-top:1px solid #333;font-size:9px;padding:15px 0 0 234px}
</style>
</head>
<body>

<section class="abs hero">
  <div class="abs hero-wheel" role="img" aria-label="Close-up photo of a dark sports car alloy wheel with red brake caliper"></div>
  <h1 class="abs">Give your car a true<br>custom look!</h1>
  <div class="abs dots"><span></span><span></span><span></span></div>
</section>

<header class="abs header">
  <div class="abs logo"><i></i>TMVG</div>
  <nav class="abs nav">
    <a class="on" href="#">Home</a><a href="#">Features</a><a href="#">Wheels</a><a href="#">Tires</a><a href="#">Store</a><a href="#">About</a><a href="#">Contacts</a>
    <svg width="10" height="10" viewBox="0 0 10 10"><circle cx="4" cy="4" r="3" fill="none" stroke="#fff" stroke-width="1.4"/><line x1="6.3" y1="6.3" x2="9" y2="9" stroke="#fff" stroke-width="1.4"/></svg>
  </nav>
  <div class="abs phone-pill">
    <svg width="9" height="9" viewBox="0 0 10 10"><path d="M2 1l2 2-1 1.5c.6 1.2 1.3 1.9 2.5 2.5L7 6l2 2-1.2 1.5C4.5 9 1 5.5.5 2.2z" fill="#fff"/></svg>0 ITEMS
  </div>
</header>

<section class="abs cats">
  <div class="cat"><div class="ph" role="img" aria-label="Silver alloy wheel photo"></div>
    <div class="cat-text"><h3>Maintenance</h3><p>Regular checks keep every wheel true, balanced and safe on the road.</p><span class="btn">Read more</span></div></div>
  <div class="cat"><div class="ph" role="img" aria-label="Chrome wheel photo"></div>
    <div class="cat-text"><h3>Wheels</h3><p>Browse a wide range of custom wheels in every finish and size.</p><span class="btn">Read more</span></div></div>
  <div class="cat"><div class="ph" role="img" aria-label="Stack of new tires photo" style="background:linear-gradient(135deg,#555,#151515)"></div>
    <div class="cat-text"><h3>Tires</h3><p>Find the right tire for any season and any driving style.</p><span class="btn">Read more</span></div></div>
</section>

<section class="abs who">
  <div class="who-text">
    <div class="eyebrow">Welcome</div>
    <h2>WHO WE ARE?</h2>
    <p class="small">We are a family run wheel and tire business. Our friendly team helps every driver find quality parts at fair prices, fitted with care and backed by honest advice.</p>
    <span class="btn red">Learn more</span>
  </div>
  <div class="ph" role="img" aria-label="Red sports coupe photo"></div>
</section>

<section class="abs finder" role="img" aria-label="Night city skyline background photo">
  <h2 class="abs">Easy Wheel &amp; Tire Finder</h2>
  <p class="abs">So we can show you the tyres and wheels that fit your vehicle.</p>
  <div class="abs selects"><div class="sel">YEAR</div><div class="sel">MODEL</div><div class="sel">MAKE</div><div class="sel">TRIM</div></div>
  <span class="abs btn red">Find</span>
</section>

<section class="abs offer">
  <div class="abs eyebrow" style="top:28px;width:1200px">Services</div>
  <h2 class="abs sec-title" style="top:40px;width:1200px">What we offer</h2>
  <div class="abs cards3" style="top:95px">
    <div class="card"><div class="ph" role="img" aria-label="Mechanic beside tire rack photo"></div>
      <div class="card-body"><h4>Multiple Options</h4><p class="small">Choose from hundreds of wheels and tires to match your car, budget and style.</p><span class="btn">Learn more</span></div></div>
    <div class="card"><div class="ph" role="img" aria-label="Wheel being installed photo"></div>
      <div class="card-body"><h4>Deliver &amp; Install</h4><p class="small">We deliver to your door or fit everything in our shop on the same day.</p><span class="btn">Learn more</span></div></div>
    <div class="card"><div class="ph" role="img" aria-label="Brake disc service photo"></div>
      <div class="card-body"><h4>Service &amp; Repairs</h4><p class="small">Balancing, alignment and repairs handled by trained, careful technicians.</p><span class="btn">Learn more</span></div></div>
  </div>
</section>

<section class="abs why">
  <div class="abs eyebrow" style="top:8px;width:1200px">Advantages</div>
  <h2 class="abs sec-title" style="top:20px;width:1200px">Why choose us</h2>
  <div class="abs ph" role="img" aria-label="Alloy wheel with tire photo"></div>
  <div class="abs num" style="top:112px;left:244px">1.</div>
  <div class="abs feat" style="top:106px;left:290px"><h4>Fast Low Cost Freight</h4><p class="small">Quick shipping at low rates to any<br>address across the country.</p></div>
  <div class="abs num" style="top:193px;left:244px">3.</div>
  <div class="abs feat" style="top:187px;left:290px"><h4>Largest Range</h4><p class="small">Thousands of wheel and tire sizes<br>ready to order from our stock.</p></div>
  <div class="abs feat" style="top:106px;left:770px"><h4>Customer Service</h4><p class="small">Friendly experts ready to help you<br>choose the best fit for your car.</p></div>
  <div class="abs num" style="top:112px;left:930px">2.</div>
  <div class="abs feat" style="top:187px;left:770px"><h4>25 Years in Business</h4><p class="small">Decades of trusted service for<br>local drivers and enthusiasts.</p></div>
  <div class="abs num" style="top:193px;left:930px">4.</div>
</section>

<section class="abs split">
  <svg class="abs" width="1200" height="399" viewBox="0 0 1200 399" role="img" aria-label="Red wheel close-up on left, tire on wet road on right">
    <defs>
      <linearGradient id="darkRoad" x1="0" y1="0" x2="1" y2="1"><stop offset="0" stop-color="#3a3a3a"/><stop offset="1" stop-color="#111"/></linearGradient>
    </defs>
    <rect width="1200" height="399" fill="url(#darkRoad)"/>
    <polygon points="0,0 634,0 569,399 0,399" fill="#b8321c"/>
  </svg>
  <div class="abs" style="top:78px;left:276px"><h2>Top<br>wheels<br>brands</h2><p>Lorem ipsum dolor sit amet, consectetur adipiscing elit. Aenean commodo.</p><span class="btn ghost">View wheels</span></div>
  <div class="abs" style="top:78px;left:689px"><h2>Find the<br>right tires</h2><p>Lorem ipsum dolor sit amet, consectetur adipiscing elit. Aenean commodo.</p><span class="btn red">View tires</span></div>
</section>

<section class="abs products" style="top:2746px;height:460px">
  <div class="abs eyebrow" style="top:0;width:1200px">Shop</div>
  <h2 class="abs sec-title" style="top:12px;width:1200px">New products</h2>
  <div class="prow" style="top:75px">
    <div class="prod"><div class="ph" role="img" aria-label="Black and gun metal wheel"></div><div class="prod-body"><h4>AXON SPC 18/20/24<br>Black and Gun Metal</h4><div class="price">$1,890 – $2,355</div><span class="btn">Details</span></div></div>
    <div class="prod"><div class="ph" role="img" aria-label="Custom painted wheel"></div><div class="prod-body"><h4>KORE SPC 18/20/24<br>Custom Painted</h4><div class="price">$1,795 – $2,290</div><span class="btn">Details</span></div></div>
    <div class="prod"><div class="ph" role="img" aria-label="Polished steel wheel"></div><div class="prod-body"><h4>TRAX SPC 18/20/24<br>Polished Steel Matt</h4><div class="price">$1,895 – $2,450</div><span class="btn">Details</span></div></div>
    <div class="prod"><div class="ph" role="img" aria-label="Polished chrome wheel"></div><div class="prod-body"><h4>LUMA SPC 18/20/24<br>Polished Chrome</h4><div class="price">$1,795 – $2,400</div><span class="btn">Details</span></div></div>
  </div>
  <span class="abs btn red" style="top:420px;left:565px">View all</span>
</section>

<section class="abs products" style="top:3206px;height:440px">
  <h2 class="abs sec-title" style="top:0;width:1200px">New products</h2>
  <div class="prow" style="top:58px">
    <div class="prod"><div class="ph" role="img" aria-label="Black and gun metal wheel"></div><div class="prod-body"><h4>AXON SPC 18/20/24<br>Black and Gun Metal</h4><div class="price">$1,890 – $2,355</div><span class="btn">Details</span></div></div>
    <div class="prod"><div class="ph" role="img" aria-label="Custom painted wheel"></div><div class="prod-body"><h4>KORE SPC 18/20/24<br>Custom Painted</h4><div class="price">$1,795 – $2,290</div><span class="btn">Details</span></div></div>
    <div class="prod"><div class="ph" role="img" aria-label="Polished steel wheel"></div><div class="prod-body"><h4>TRAX SPC 18/20/24<br>Polished Steel Matt</h4><div class="price">$1,895 – $2,450</div><span class="btn">Details</span></div></div>
    <div class="prod"><div class="ph" role="img" aria-label="Polished chrome wheel"></div><div class="prod-body"><h4>LUMA SPC 18/20/24<br>Polished Chrome</h4><div class="price">$1,795 – $2,400</div><span class="btn">Details</span></div></div>
  </div>
  <span class="abs btn red" style="top:405px;left:565px">View all</span>
</section>

<section class="abs video" role="img" aria-label="Tire and gloved hand background photo">
  <h2 class="abs">Don't have to</h2>
  <div class="abs vbox">
    <div class="ph" role="img" aria-label="Technician fitting a wheel video still"></div>
    <div class="abs play"><svg width="40" height="28" viewBox="0 0 40 28"><polygon points="16,8 26,14 16,20" fill="#fff"/></svg></div>
    <p>Over 500 fee tools to ensure you get the perfect tire for your vehicle.</p>
    <div style="text-align:center"><span class="btn red">Watch video guide</span></div>
  </div>
</section>

<section class="abs cust">
  <div class="abs eyebrow" style="top:0;width:1200px">Recent</div>
  <h2 class="abs sec-title" style="top:12px;width:1200px">Our customers</h2>
  <div class="abs row">
    <div class="ph" role="img" aria-label="Happy customer in car photo"></div>
    <div class="ph" role="img" aria-label="Customer checking a tire photo"></div>
    <div class="ph" role="img" aria-label="Customer driving photo"></div>
  </div>
  <span class="abs btn red" style="top:266px;left:518px">View all testimonials</span>
</section>

<section class="abs partners">
  <div class="badge"></div><div class="badge"></div><div class="badge"></div><div class="badge"></div><div class="badge"></div><div class="badge"></div>
</section>

<footer class="abs footer">
  <div class="abs fcol" style="left:234px;width:170px">
    <div class="flogo"><i></i>TMVG</div>
    <p>Quality wheels and tires fitted by local experts who care about your ride.</p>
  </div>
  <div class="abs fcol" style="left:430px">
    <h4>Links</h4>
    <div class="flinks"><ul><li>Home</li><li>Features</li><li>Wheels</li></ul><ul><li>Tires</li><li>Store</li><li>Contacts</li></ul></div>
  </div>
  <div class="abs fcol" style="left:610px">
    <h4>Contact Us</h4>
    <p>(555) 013-2048<br>42 Harbor Lane, Springfield<br>info@tmvg.example</p>
  </div>
  <div class="abs fcol" style="left:796px">
    <h4>Get Our Newsletter</h4>
    <div class="news"><span class="news-field">Email</span><span class="btn red">Go</span></div>
  </div>
  <div class="abs fbar">TMVG © 2024. All rights reserved.</div>
</footer>

</body>
</html>
```